Target Market(s)

Corporate

Colors

Designer to choose colors to be used in the design.

Requirements
Must have
• An Overview / Background of the Business & Services- Company Name: UMM TALIAFOR NEXIRO WORKS W prefer as UMM TALIA. Umm Talia offers specialized services in Network information security services, data center & Network infrastructure, data caption & security services, software services. Umm Talia provides wide range of services that helps the organization in their business priorities strategies. Umm Talia specialized team has handles prestigious projects & executed with ease.
• * The Target Market / Audience you are trying to reach – corporate We are doing CCTV supply & Service, cabling supply & Services , PI system supply & Service, BMS supply & Service, Fire & safety supply & services. we are basically target corporates ,malls, enterprise users and governments.
• * Design Specifics; any preferences or ideas for Style, Colour, Imagery, etc- We prefer mild & unique color.
Nice to have
• Mild and unique color

```html
<!DOCTYPE html>
<html lang="en">
<head>
<meta charset="utf-8">
<title>Umm Talia Letterhead</title>
<link rel="stylesheet" href="https://fonts.googleapis.com/css2?family=Mulish:wght@400;500&display=swap">
<style>
  :root {
    --backdrop: #d9d9d9;
    --paper: #ececec;
    --ink: #1f1f1f;
    --muted: #3a3a3a;
    --brand-red: #c8262a;
    --deep-red: #8c1c1c;
    --orange: #f07b22;
    --amber: #f7a823;
    --rule: #b9b9b9;
  }
  * { box-sizing: border-box; margin: 0; padding: 0; }
  html, body {
    width: 1116px; height: 1200px; overflow: hidden;
    background: var(--backdrop);
    font-family: "Mulish", Arial, sans-serif;
    color: var(--ink);
  }
  .letterhead {
    position: absolute; left: 121px; top: 0;
    width: 874px; height: 1200px;
    background: var(--paper);
    overflow: hidden;
  }
  .brand { position: absolute; left: 730px; top: 18px; width: 110px; text-align: center; }
  .brand-square { width: 84px; height: 84px; background: var(--brand-red); margin: 0 auto; }
  .brand-name { margin-top: 6px; font-size: 15px; font-weight: 500; color: var(--brand-red); letter-spacing: 0.5px; white-space: nowrap; }

  .letter-body { position: absolute; left: 87px; top: 133px; width: 730px; font-size: 15.4px; line-height: 20px; }
  .salutation { margin-bottom: 20px; }
  .paragraph { margin-bottom: 20px; }
  .paragraph .line { display: block; white-space: nowrap; }
  .closing { margin-top: 0; }

  .signature-mark { position: absolute; left: 215px; top: 801px; width: 106px; height: 22px; background: linear-gradient(90deg, rgba(60,60,60,0.15), rgba(60,60,60,0.45), rgba(60,60,60,0.15)); border-radius: 11px; }
  .signer { position: absolute; left: 220px; top: 832px; width: 190px; text-align: right; }
  .signer-name { font-size: 26px; line-height: 30px; color: var(--muted); white-space: nowrap; }
  .signer-role { font-size: 12px; color: var(--orange); line-height: 14px; }

  .pattern-block { position: absolute; left: 0; top: 883px; width: 256px; height: 317px; background: linear-gradient(160deg, var(--orange) 0%, var(--brand-red) 45%, var(--deep-red) 70%, var(--amber) 100%); opacity: 0.9; }

  .contact-bar { position: absolute; left: 293px; top: 1048px; width: 581px; display: flex; height: 17px; }
  .contact-bar span { color: #fff; font-size: 11.5px; line-height: 17px; text-align: center; }
  .tab-phone { width: 123px; background: var(--deep-red); }
  .tab-email { width: 120px; background: var(--brand-red); }
  .tab-web { width: 125px; background: var(--orange); }
  .tab-address { width: 213px; background: var(--amber); }

  .contact-details { position: absolute; left: 293px; top: 1072px; width: 581px; display: flex; font-size: 11px; line-height: 15px; color: var(--muted); }
  .detail { padding-top: 3px; white-space: nowrap; }
  .detail + .detail { border-left: 1px solid var(--rule); min-height: 58px; }
  .detail-phone { width: 123px; text-align: center; }
  .detail-email { width: 120px; text-align: center; padding-top: 12px; }
  .detail-web { width: 125px; text-align: center; padding-top: 12px; }
  .detail-address { width: 213px; padding-left: 13px; }
</style>
</head>
<body>
<main class="letterhead">
  <header class="brand">
    <div class="brand-square"></div>
    <div class="brand-name">UMM TALIA</div>
  </header>

  <section class="letter-body">
    <p class="salutation">Dear sir / madam,</p>
    <p class="paragraph">
      <span class="line">Lorem ipsum dolor sit amet, consectetur adipisicing elit, sed do eiusmod tempor incididunt</span>
      <span class="line">ut labore et dolore magna aliqua. Ut enim ad minim veniam, quis nostrud exercitation ulla-</span>
      <span class="line">mco laboris nisi ut aliquip ex ea commodo consequat. Duis aute irure dolor in reprehenderit</span>
      <span class="line">in voluptate velit esse cillum dolore eu fugiat nulla pariatur. Excepteur sint occaecat cupid-</span>
      <span class="line">atat non proident, sunt in culpa qui officia deserunt mollit anim id est laborum.</span>
    </p>
    <p class="paragraph">
      <span class="line">Lorem ipsum dolor sit amet, consectetur adipisicing elit, sed do eiusmod tempor incididunt</span>
      <span class="line">ut labore et dolore magna aliqua. Ut enim ad minim veniam, quis nostrud exercitation ulla-</span>
      <span class="line">mco laboris nisi ut aliquip ex ea commodo consequat. Duis aute irure dolor in reprehenderit</span>
      <span class="line">in voluptate velit esse cillum dolore eu fugiat nulla pariatur. Excepteur sint occaecat cupid-</span>
      <span class="line">atat non proident, sunt in culpa qui officia deserunt mollit anim id est laborum.</span>
    </p>
    <p class="paragraph">
      <span class="line">Lorem ipsum dolor sit amet, consectetur adipisicing elit, sed do eiusmod tempor incididunt</span>
      <span class="line">ut labore et dolore magna aliqua. Ut enim ad minim veniam, quis nostrud exercitation ulla-</span>
      <span class="line">mco laboris nisi ut aliquip ex ea commodo consequat. Duis aute irure dolor in reprehenderit</span>
      <span class="line">in voluptate velit esse cillum dolore eu fugiat nulla pariatur. Excepteur sint occaecat cupid-</span>
      <span class="line">atat non proident, sunt in culpa qui officia deserunt mollit anim id est laborum.</span>
    </p>
    <p class="paragraph">
      <span class="line">Lorem ipsum dolor sit amet, consectetur adipisicing elit, sed do eiusmod tempor incididunt</span>
      <span class="line">ut labore et dolore magna aliqua. Ut enim ad minim veniam, quis nostrud exercitation ulla-</span>
      <span class="line">mco laboris nisi ut aliquip ex ea commodo consequat. Duis aute irure dolor in reprehenderit</span>
      <span class="line">in voluptate velit esse cillum dolore eu fugiat nulla pariatur. Excepteur sint occaecat cupid-</span>
      <span class="line">atat non proident, sunt in culpa qui officia deserunt mollit anim id est laborum.</span>
    </p>
    <p class="paragraph">
      <span class="line">Lorem ipsum dolor sit amet, consectetur adipisicing elit, sed do eiusmod tempor incididunt</span>
      <span class="line">ut labore et dolore magna aliqua. Ut enim ad minim veniam, quis nostrud exercitation ulla-</span>
      <span class="line">mco laboris nisi ut aliquip ex ea commodo consequat. Duis aute irure dolor in reprehenderit</span>
      <span class="line">in voluptate velit esse cillum dolore eu fugiat nulla pariatur. Excepteur sint occaecat cupid-</span>
      <span class="line">atat non proident, sunt in culpa qui officia deserunt mollit anim id est laborum.</span>
    </p>
    <p class="closing">Yours Sincerely,</p>
  </section>

  <div class="signature-mark" role="img" aria-label="Handwritten signature"></div>
  <div class="signer">
    <div class="signer-name">Layla Haddad</div>
    <div class="signer-role">CEO</div>
  </div>

  <div class="pattern-block" role="img" aria-label="Decorative pattern of red, orange and yellow squares with white circles"></div>

  <div class="contact-bar">
    <span class="tab-phone">Phone &amp; Fax</span>
    <span class="tab-email">Email</span>
    <span class="tab-web">Website</span>
    <span class="tab-address">Address</span>
  </div>
  <footer class="contact-details">
    <div class="detail detail-phone">800-555-0142<br>800-555-0187</div>
    <div class="detail detail-email">l.haddad@nexiro.org</div>
    <div class="detail detail-web">www.nexiro.org</div>
    <div class="detail detail-address">Nexiro Works<br>2217 Harbor Road<br>Suite 40, West Bay,<br>QATAR</div>
  </footer>
</main>
</body>
</html>
```